We sell companies excess stock for them

We need a business card for a company based in New Zealand called 'ShelfLark'.

Check out our website to get an idea www.shelflark.example

We help other businesses to;
- Sell Excess Stock
- Manage Product Returns
- Sell Company Assets

Our logo is attached for your reference
The font used is 'RifficFree-Bold'

Target Market(s)

Businesses

Industry/Entity Type

Business

Contact Information for Business Card

Name: Mara Quillby
Phone: 027 864 3190
email: maraquillby@shelflark.example
website: www.shelflark.example

Font styles to use
Other font styles liked:

Colors
9bcb3b

Requirements
Must have
Nice to have
Should not have

```html
<!DOCTYPE html>
<html lang="en">
<head>
<meta charset="utf-8">
<title>ShelfLark business card</title>
<link href="https://fonts.googleapis.com/css2?family=Fredoka:wght@600;700&family=Open+Sans:wght@400;600&display=swap" rel="stylesheet">
<style>
  :root {
    --page: #e4e4e4;
    --card-light: #fbfbfb;
    --card-shade: #dcdcdc;
    --ink: #2f2c2b;
    --band: #332f2e;
    --green: #9bcb3b;
    --dot: #cfcfcf;
    --art-warm: #e69a2a;
    --art-green: #7fbf3a;
  }
  html, body {
    margin: 0;
    width: 1200px;
    height: 900px;
    overflow: hidden;
    background: var(--page);
  }
  .canvas {
    position: relative;
    width: 1200px;
    height: 900px;
  }
  .card {
    position: absolute;
    width: 640px;
    height: 366px;
    border-radius: 28px;
    overflow: hidden;
    background: radial-gradient(ellipse at 60% 30%, var(--card-light) 0%, #efefef 55%, var(--card-shade) 100%);
    box-shadow: 0 10px 24px rgba(0,0,0,0.18);
  }
  .card--front { left: 90px; top: 50px; }
  .card--back { left: 470px; top: 484px; }

  /* front */
  .mascot-art {
    position: absolute;
    left: 0;
    top: 40px;
    width: 250px;
    height: 326px;
    background: linear-gradient(160deg, #f1d7a6 0%, var(--art-warm) 45%, var(--art-green) 100%);
    border-top-right-radius: 120px;
  }
  .front-band {
    position: absolute;
    left: 250px;
    right: 0;
    bottom: 0;
    height: 88px;
    background: var(--band);
  }
  .band-dots {
    position: absolute;
    display: flex;
    gap: 5px;
  }
  .band-dots span {
    width: 11px;
    height: 11px;
    border-radius: 50%;
    background: var(--dot);
  }
  .band-dots span.is-active { background: var(--green); }
  .card--front .band-dots { right: 26px; top: 24px; }

  .holder-name {
    position: absolute;
    left: 272px;
    top: 150px;
    margin: 0;
    font-family: "Fredoka", sans-serif;
    font-weight: 700;
    font-size: 50px;
    letter-spacing: -1px;
    line-height: 1;
    color: var(--ink);
  }
  .holder-name .surname { color: var(--green); }
  .contact {
    position: absolute;
    left: 274px;
    top: 212px;
    font-family: "Open Sans", sans-serif;
    font-size: 14px;
    color: var(--ink);
    line-height: 1.45;
  }
  .contact-row { display: flex; align-items: center; gap: 6px; }
  .contact-row svg { width: 12px; height: 12px; flex: none; }
  .contact-row .gap { width: 10px; }
  .contact-web { display: block; }
  .contact .site { color: var(--green); font-weight: 600; }

  /* back */
  .logo-art {
    position: absolute;
    left: 270px;
    top: 70px;
    width: 110px;
    height: 80px;
    border-radius: 40px 40px 20px 20px;
    background: linear-gradient(150deg, var(--art-green) 0%, var(--art-warm) 100%);
  }
  .wordmark {
    position: absolute;
    left: 0;
    right: 0;
    top: 168px;
    margin: 0;
    text-align: center;
    font-family: "Fredoka", sans-serif;
    font-weight: 700;
    font-size: 60px;
    letter-spacing: -1px;
    line-height: 1;
    color: var(--ink);
  }
  .services {
    position: absolute;
    left: 0;
    right: 0;
    top: 238px;
    margin: 0;
    padding: 0;
    list-style: none;
    display: flex;
    justify-content: center;
    gap: 14px;
    font-family: "Open Sans", sans-serif;
    font-size: 14px;
    color: #555;
  }
  .services li::before {
    content: "";
    display: inline-block;
    width: 5px;
    height: 5px;
    border-radius: 50%;
    background: var(--green);
    margin-right: 6px;
    vertical-align: middle;
  }
  .back-band {
    position: absolute;
    left: 0;
    right: 0;
    bottom: 0;
    height: 48px;
    background: var(--band);
  }
  .card--back .band-dots { left: 50%; transform: translateX(-50%); bottom: 72px; }
</style>
</head>
<body>
<main class="canvas">
  <section class="card card--front" aria-label="Card front">
    <div class="mascot-art" role="img" aria-label="Illustrated delivery mascot carrying a parcel and giving a thumbs up"></div>
    <div class="front-band">
      <div class="band-dots"><span></span><span></span><span class="is-active"></span></div>
    </div>
    <h1 class="holder-name">Mara<span class="surname">Quillby</span></h1>
    <div class="contact">
      <div class="contact-row">
        <svg viewBox="0 0 12 12" aria-hidden="true"><path d="M3 1 L5 3.5 L4 5 Q5.5 7 7 8 L8.5 7 L11 9 L9.5 11 Q4 10 1 3 Z" fill="#9bcb3b"/></svg>
        <span>027 864 3190</span>
        <span class="gap"></span>
        <svg viewBox="0 0 12 12" aria-hidden="true"><rect x="1" y="2.5" width="10" height="7" rx="1" fill="#9bcb3b"/><path d="M1.5 3 L6 6.5 L10.5 3" stroke="#fff" stroke-width="1" fill="none"/></svg>
        <span>maraquillby@shelflark.example</span>
      </div>
      <div class="contact-web">www.<span class="site">shelflark</span>.example</div>
    </div>
  </section>

  <section class="card card--back" aria-label="Card back">
    <div class="logo-art" role="img" aria-label="Small mascot illustration above the company name"></div>
    <p class="wordmark">ShelfLark</p>
    <ul class="services">
      <li>Excess Stock</li>
      <li>Asset Sales</li>
      <li>Product Returns</li>
    </ul>
    <div class="band-dots"><span></span><span class="is-active"></span><span></span></div>
    <div class="back-band"></div>
  </section>
</main>
</body>
</html>
```